Website page design

Hi, I need to improve the look of my homepage and the final offer page of my website. www.Pebble7dock.com We have an orvex buyback program where we purchase used orvex products from consumers nationwide. If you would go click through a sample offer on the site, you will the last view final offer page where we give you a cash offer for you site. I would like to keep the red and white colors since my logo is red and white. Please pay attention to the information shown on the homepage now, it is important for me to show the visitors this information on the home page. I would also love to give the users a friendly and inviting look when clicking on the options of orvex products on the home page.

Target Market(s)

Orvex electronics consumers

Number of Pages Required

2 page

Requirements
Nice to have
• On the final offer page, i would love for the offer to give an exciting look for the pebble 7 dock offer, and a boring look for the orvex buy back offer. At the final offer page you will my websites offer ( Your Pebble7dock Offer ) vs ( Orvex buyback program offer ) which is my competitor.

```html
<!DOCTYPE html>
<html lang="en">
<head>
<meta charset="utf-8">
<title>Pebble7dock – Final Offer</title>
<link rel="stylesheet" href="https://fonts.googleapis.com/css2?family=Montserrat:wght@400;500;600;700&family=Jost:wght@400;500&display=swap">
<style>
:root{
  --red:#c9222c;
  --red-dark:#5e1015;
  --black:#000;
  --green:#3aaa6a;
  --green-btn:#3fae5a;
  --panel:#ededed;
  --cell:#efefef;
  --footer:#3a3a3a;
  --text:#333;
  --white:#fff;
}
*{margin:0;padding:0;box-sizing:border-box}
html,body{width:877px;height:1200px;overflow:hidden;background:var(--white)}
body{position:relative;font-family:"Montserrat",sans-serif;color:var(--text)}
.abs{position:absolute}

/* header */
.site-header{left:0;top:0;width:877px;height:62px;background:var(--red)}
.brand{left:103px;top:12px;display:flex;align-items:center;gap:14px}
.brand-mark{width:44px;height:37px;background:var(--white);display:flex;align-items:center;justify-content:center}
.brand-mark span{width:30px;height:23px;background:var(--red)}
.brand-name{font-family:"Jost",sans-serif;font-size:21px;color:var(--white);letter-spacing:1.5px}
.main-nav{right:103px;top:19px;display:flex;align-items:center;gap:22px;font-family:"Jost",sans-serif;font-size:12px;color:var(--white)}
.main-nav a{color:var(--white);text-decoration:none;display:flex;align-items:center;gap:5px}
.main-nav .login{background:var(--green-btn);padding:6px 14px}

/* hero */
.hero{left:0;top:62px;width:877px;height:255px;overflow:hidden}
.hero-title{right:143px;top:42px;text-align:right;font-weight:700;font-size:19.5px;line-height:29.5px;color:var(--white);letter-spacing:.3px}
.hero-photo{left:128px;top:5px;width:200px;height:250px;border-radius:90px 90px 0 0;background:linear-gradient(180deg,#8a4a2c,#d84550 55%,#c62c36)}
.badges{left:398px;top:228px;display:flex;gap:18px}
.badges span{width:56px;height:34px;border-radius:4px;background:#3b3b3b}
.badges span.wide{width:104px}

/* specs */
.specs{left:103px;top:354px;width:671px;height:49px;display:flex;background:var(--cell)}
.specs div{flex:1;text-align:center;padding-top:8px;font-size:8px;color:#222;border-right:1px solid #e0e0e0;line-height:10px}
.specs div:last-child{border:0}
.specs b{display:block;font-weight:400;color:var(--red);font-size:10px;margin-bottom:2px}

/* condition */
.section-title{left:0;width:877px;top:432px;text-align:center;font-weight:600;font-size:25px;color:#000}
.title-rule{left:424px;top:470px;width:29px;height:1px;background:#ccc}
.conditions{left:103px;top:498px;width:672px;display:grid;grid-template-columns:repeat(3,209px);column-gap:22px;row-gap:24px}
.condition{height:59px;background:var(--red);color:var(--white);font-weight:600;font-size:12px;letter-spacing:.8px;display:flex;align-items:center;justify-content:center}
.condition.is-selected{background:var(--black)}

/* offers */
.offer-shapes{left:103px;top:695px}
.offer-label{font-size:12.5px;letter-spacing:.4px;color:#333;display:flex;align-items:center;gap:6px}
.offer-price{font-family:"Jost",sans-serif;font-weight:500;font-size:34px;color:var(--green);text-align:center}
.offer-ours{left:150px;top:728px;width:180px;text-align:center}
.offer-ours .offer-label{justify-content:center}
.sell-now{display:inline-block;margin-top:4px;background:var(--green-btn);color:var(--white);font-size:11px;font-weight:500;padding:5px 9px;letter-spacing:.4px}
.offer-valid{margin-top:12px;font-size:10px;letter-spacing:.4px}
.offer-theirs{left:528px;top:728px;width:210px;text-align:center}
.vs{left:407px;top:751px;width:62px;height:62px;border-radius:50%;background:var(--red);color:var(--white);font-weight:700;font-size:15px;display:flex;align-items:center;justify-content:center;box-shadow:0 0 0 7px #f5f5f5}

/* footer */
.site-footer{left:0;top:940px;width:877px;height:260px;background:var(--footer);color:var(--white);font-family:"Jost",sans-serif}
.f-brand{left:103px;top:72px;display:flex;align-items:center;gap:12px}
.f-brand .brand-mark{width:40px;height:33px}
.f-brand .brand-mark span{width:26px;height:20px}
.f-brand .brand-name{font-size:16px;letter-spacing:4px}
.f-about{left:104px;top:120px;width:180px;font-size:9.5px;line-height:15px}
.f-about em{font-style:normal;color:var(--red)}
.f-divider{top:68px;width:1px;height:100px;background:#555}
.f-col h3{font-size:12.5px;font-weight:500;letter-spacing:.2px}
.f-col .rule{margin-top:9px;height:1px;background:#5a5a5a;position:relative}
.f-col .rule::before{content:"";position:absolute;left:0;top:0;width:23px;height:2px;background:var(--white)}
.f-links{list-style:none;margin-top:11px;font-size:9.5px;line-height:17px}
.contact-row,.social-row{display:flex;gap:10px;font-size:9.5px;line-height:14px;margin-top:11px;align-items:flex-start}
.icon-ring{width:20px;height:20px;border:1px solid #ddd;border-radius:50%;flex:none;display:flex;align-items:center;justify-content:center}
.contact-row .name{color:var(--red);font-size:10.5px}
.f-bottom-rule{left:103px;top:217px;width:671px;height:1px;background:#4a4a4a}
.copyright{left:0;width:877px;top:233px;text-align:center;font-size:10px}
</style>
</head>
<body>

<header class="site-header abs">
  <div class="brand abs"><div class="brand-mark"><span></span></div><div class="brand-name">PEBBLE7DOCK</div></div>
  <nav class="main-nav abs">
    <a href="#"><svg width="11" height="11" viewBox="0 0 12 12" fill="none" stroke="#fff" stroke-width="1.3"><path d="M1 2h2l1.5 6h6L12 4H4"/><circle cx="5" cy="10.5" r="1"/><circle cx="10" cy="10.5" r="1"/></svg>Sell</a>
    <a href="#"><svg width="11" height="11" viewBox="0 0 12 12" fill="none" stroke="#fff" stroke-width="1.3"><circle cx="6" cy="6" r="5"/><path d="M1 6h10M6 1c2 2 2 8 0 10M6 1c-2 2-2 8 0 10"/></svg>Track</a>
    <a href="#"><svg width="12" height="11" viewBox="0 0 12 11" fill="#fff"><circle cx="5" cy="3" r="2.5"/><path d="M0 11c0-4 10-4 10 0z"/><path d="M10 3v4M8 5h4" stroke="#fff"/></svg>Join</a>
    <a href="#" class="login"><svg width="10" height="10" viewBox="0 0 10 10" fill="#fff"><path d="M0 4h5V2l3 3-3 3V6H0z"/><path d="M6 0h4v10H6V9h3V1H6z"/></svg>Login</a>
  </nav>
</header>

<section class="hero abs">
  <svg class="abs" width="877" height="255" viewBox="0 0 877 255">
    <rect width="877" height="255" fill="#000"/>
    <polygon points="0,125 0,255 115,255" fill="var(--red)"/>
    <polygon points="90,0 310,0 560,255 340,255" fill="var(--red-dark)"/>
    <polygon points="340,255 560,255 515,210 300,210" fill="var(--red)" opacity=".0"/>
    <polygon points="770,0 877,0 877,155" fill="var(--red)"/>
    <polygon points="470,190 530,255 560,255 500,190" fill="var(--red)"/>
    <line x1="88" y1="0" x2="340" y2="255" stroke="var(--red)" stroke-width="1.5"/>
    <line x1="560" y1="212" x2="600" y2="255" stroke="var(--red)" stroke-width="1.5"/>
    <line x1="670" y1="0" x2="700" y2="32" stroke="var(--red)" stroke-width="1.5"/>
    <polyline points="318,14 772,14 772,227 318,227" fill="none" stroke="#5a5a5a" stroke-width="4"/>
  </svg>
  <div class="hero-photo abs" role="img" aria-label="Smiling customer holding cash and a phone"></div>
  <h1 class="hero-title abs">WE HAVE AN ORVEX BUYBACK<br>PROGRAM WHERE WE PURCHASE<br>USED ORVEX PRODUCTS FROM<br>CONSUMERS NATIONWIDE</h1>
  <div class="badges abs"><span></span><span class="wide" style="width:74px"></span><span></span><span class="wide"></span></div>
</section>

<div class="specs abs">
  <div><b>Device</b>OrvexBook</div>
  <div><b>Model</b>17" Pro</div>
  <div><b>Processor</b>3..6Ghz Dual Core<br>(2009</div>
  <div><b>Hard Drive</b>500 GB</div>
  <div><b>Memory</b>4GB</div>
  <div><b>Accessories</b>4GB</div>
</div>

<h2 class="section-title abs">SELECT CONDITION</h2>
<div class="title-rule abs"></div>
<div class="conditions abs">
  <div class="condition">Sealed</div>
  <div class="condition">Flawless</div>
  <div class="condition is-selected">Normal</div>
  <div class="condition">Fair</div>
  <div class="condition">Cracked</div>
  <div class="condition">Broken</div>
</div>

<svg class="offer-shapes abs" width="672" height="245" viewBox="0 0 672 245">
  <defs>
    <linearGradient id="fade" x1="0" y1="0" x2="0" y2="1">
      <stop offset="0" stop-color="#ededed" stop-opacity=".6"/>
      <stop offset="1" stop-color="#ededed" stop-opacity="0"/>
    </linearGradient>
  </defs>
  <path d="M10 0H266L318 70 318 105 266 175H10Q0 175 0 165V10Q0 0 10 0Z" fill="var(--panel)"/>
  <path d="M662 0H404L352 70 352 105 404 175H662Q672 175 672 165V10Q672 0 662 0Z" fill="var(--panel)"/>
  <path d="M0 175H266L318 245H0Z" fill="url(#fade)"/>
  <path d="M672 175H404L352 245H672Z" fill="url(#fade)"/>
</svg>

<div class="offer-ours abs">
  <div class="offer-label"><svg width="12" height="12" viewBox="0 0 12 12" fill="none" stroke="var(--green)" stroke-width="1.4"><rect x=".7" y="1.7" width="9.6" height="9.6"/><path d="M3 6l2.5 2.5L11.5 1"/></svg>Your Pebble7dock Offer</div>
  <div class="offer-price">$201</div>
  <a class="sell-now">Sell Now</a>
  <div class="offer-valid">Offer Valid For 30 Day</div>
</div>
<div class="vs abs">VS</div>
<div class="offer-theirs abs">
  <div class="offer-label"><svg width="13" height="13" viewBox="0 0 13 13" fill="none" stroke="var(--red)" stroke-width="1.4"><rect x=".7" y=".7" width="11.6" height="11.6"/><path d="M4 4l5 5M9 4l-5 5"/></svg>Orvex Buyback Program Offer</div>
  <div class="offer-price" style="margin-top:10px">$100</div>
</div>

<footer class="site-footer abs">
  <div class="f-brand abs"><div class="brand-mark"><span></span></div><div class="brand-name">PEBBLE7DOCK</div></div>
  <p class="f-about abs">Lorem ipsum dolor sit amet, consectetuer adipiscing elit, sed diam nonummy nibh euismod tincidunt ut laoreet dolore magna aliquam erat volutpat...<em>Read More »</em></p>
  <div class="f-divider abs" style="left:309px"></div>
  <div class="f-divider abs" style="left:455px"></div>
  <div class="f-divider abs" style="left:647px"></div>

  <div class="f-col abs" style="left:340px;top:52px;width:87px">
    <h3>QUICK LINKS</h3><div class="rule"></div>
    <ul class="f-links"><li>• About Us</li><li>• FAQ's</li><li>• Terms of Service</li><li>• Privacy Policy</li><li>• Contact Us</li></ul>
  </div>

  <div class="f-col abs" style="left:485px;top:52px;width:129px">
    <h3>CONTACT DETAILS</h3><div class="rule"></div>
    <div class="contact-row"><span class="icon-ring"><svg width="8" height="10" viewBox="0 0 8 10" fill="none" stroke="#fff"><path d="M4 9.5S.5 6 .5 4a3.5 3.5 0 017 0c0 2-3.5 5.5-3.5 5.5z"/><circle cx="4" cy="4" r="1"/></svg></span><div><span class="name">PEBBLE7DOCK</span><br>48 Linden Crescent,<br>Maple Falls, NY, 10890</div></div>
    <div class="contact-row" style="align-items:center"><span class="icon-ring"><svg width="9" height="9" viewBox="0 0 10 10" fill="#fff"><path d="M2 0l2 2.5-1 1.2c.6 1.3 1.6 2.3 2.9 2.9l1.2-1L10 8l-1.5 2C4 10 0 6 0 1.5z"/></svg></span>555-204-7731</div>
    <div class="contact-row" style="align-items:center;margin-top:18px"><span class="icon-ring"><svg width="10" height="8" viewBox="0 0 10 8" fill="#fff"><path d="M0 0h10v1L5 4 0 1zM0 2l5 3 5-3v6H0z"/></svg></span>Info@pebble7dock.com</div>
  </div>

  <div class="f-col abs" style="left:677px;top:52px;width:97px">
    <h3>FOLLOW US ON</h3><div class="rule"></div>
    <div class="social-row" style="align-items:center;margin-top:14px"><span class="icon-ring"></span>Chatterly</div>
    <div class="social-row" style="align-items:center;margin-top:9px"><span class="icon-ring"></span>Picturo</div>
  </div>

  <div class="f-bottom-rule abs"></div>
  <p class="copyright abs">Copyright © 2019 PEBBLE7DOCK. All Rights Reserved.</p>
</footer>

</body>
</html>
```